Brindle Structures Construction Company Seeking Modern Website

We are a small construction company wanting to create a web presence. We don't have much in the way of current content but will get photos as they come in. Attached is a picture of our business card.
The pages we would like on the menu are:
Home
Portfolio
Product Specs
Testimonials
Our Process
Contact
Some designs we like are:
http://www.tovenquarnsheds.example/
http://www.qzrsheds.example/
http://pannowsheds.example/
http://wistenhalls.example/
Not much requirements other than that so feel free to be creative!
Updates
Target Market(s)
Construction
Commercial and Residential Buildings
Industry/Entity Type
Construction Company
Number of Pages Required
5+ page
Look and feel

```html
<!DOCTYPE html>
<html lang="en">
<head>
<meta charset="utf-8">
<title>Brindle Structures</title>
<link href="https://fonts.googleapis.com/css2?family=Lato:ital,wght@0,400;0,700;1,400;1,700&display=swap" rel="stylesheet">
<style>
:root{
  --blue:#1b9ad6;
  --red:#d9261c;
  --text:#555;
  --dark:#2d2d2d;
  --grey-band:#ececec;
  --line:#e3e3e3;
}
*{margin:0;padding:0;box-sizing:border-box}
html,body{width:882px;height:1200px;overflow:hidden;background:#fff;font-family:'Lato',sans-serif;color:var(--text)}
.page{position:relative;width:882px;height:1200px;border-top:3px solid var(--blue)}
.header{height:75px;position:relative}
.brand{position:absolute;left:96px;top:20px;font-size:27px;font-weight:700;color:var(--red);display:flex;align-items:center;gap:8px}
.brand-mark{width:14px;height:14px;border-radius:50%;background:var(--blue)}
.call{position:absolute;right:96px;top:30px;font-size:14px;display:flex;align-items:center;gap:12px}
.call em{font-style:italic;font-weight:700;color:#666}
.call .phone{color:var(--blue);font-weight:700;display:flex;align-items:center;gap:5px;font-size:13px}
.nav{height:34px;border-top:1px solid var(--line);border-bottom:1px solid var(--line);display:flex;justify-content:center}
.nav ul{list-style:none;display:flex;border-left:1px solid var(--line)}
.nav li{width:115px;text-align:center;font-size:11px;line-height:32px;color:#666;border-right:1px solid var(--line)}
.nav li.active{color:var(--red)}
.hero{position:relative;height:334px;overflow:hidden}
.hero-photo{position:absolute;inset:0;background:linear-gradient(100deg,#1c8fc0 0%,#37b4e0 40%,#5ccbee 60%,#2d6a90 100%)}
.hero h1{position:absolute;left:97px;top:42px;font-size:28px;font-weight:400;line-height:39px;color:#fff;text-shadow:0 2px 4px rgba(0,0,0,.3)}
.hero svg{position:absolute;left:0;bottom:0}
.dots{position:absolute;left:415px;top:304px;display:flex;gap:5px}
.dots span{width:9px;height:9px;border-radius:50%;background:#ddd}
.dots span.on{background:var(--red)}
.welcome{text-align:center;padding-top:36px}
.welcome h2{font-size:22px;font-weight:400;color:#777;letter-spacing:.3px}
.welcome h2 b{color:var(--blue);font-weight:400}
.welcome p{width:665px;margin:14px auto 0;font-size:11px;line-height:16px;color:#666}
.more{display:inline-block;margin-top:20px;font-size:11px;font-weight:700;color:var(--blue)}
.cards{position:absolute;top:638px;left:96px;display:flex;gap:25px}
.card{width:213px;height:222px;border:1px solid var(--line);border-top:3px solid var(--blue);background:#fff;padding:10px 11px;box-shadow:0 8px 8px -6px rgba(0,0,0,.15)}
.card-title{display:flex;align-items:center;gap:8px;font-size:14px;color:var(--blue);margin-bottom:10px}
.icon{width:27px;height:27px;border-radius:50%;background:var(--red);display:flex;align-items:center;justify-content:center}
.news{display:flex;gap:8px;padding-bottom:6px;margin-bottom:6px;border-bottom:1px dotted #bbb}
.news:last-of-type{border:none}
.date{width:26px;height:28px;background:#333;color:#fff;text-align:center;font-size:11px;line-height:13px;padding-top:2px;flex:none}
.date small{display:block;font-size:7px;background:#222}
.news h4,.task h4{font-size:9.5px;color:#333;font-weight:700}
.news p,.task p{font-size:8.5px;line-height:13px;color:#555}
.link{text-align:right;font-size:8.5px;font-weight:700;color:var(--blue)}
.task{display:flex;gap:8px;padding-bottom:8px;margin-bottom:8px;border-bottom:1px dashed #ccc}
.task:last-of-type{border:none}
.task h4{font-size:10.5px;font-weight:400;color:#333;margin-bottom:2px}
.person{display:flex;align-items:center;gap:12px;margin-top:2px}
.avatar{width:63px;height:63px;border-radius:50%;border:3px solid var(--blue);background:#c9a48d}
.person b{font-size:11px;color:#333;font-weight:700;display:block}
.person span{font-size:9px}
.quote{margin-top:16px;border:1px solid var(--line);padding:8px 10px;font-size:10px;line-height:17px;font-style:italic;color:#444;position:relative}
.quote .qd{position:absolute;right:10px;bottom:6px;display:flex;gap:3px}
.quote .qd i{width:5px;height:5px;border-radius:50%;background:#ccc}
.quote .qd i.on{background:var(--red)}
.types{position:absolute;top:893px;left:0;width:882px;height:200px;background:var(--grey-band)}
.ribbon{position:absolute;left:352px;top:0;width:178px;height:25px;background:var(--red);color:#fff;font-size:15px;text-align:center;line-height:25px;clip-path:polygon(0 0,100% 0,94% 100%,6% 100%)}
.gallery{position:absolute;top:53px;left:98px;display:flex;gap:9px}
.tile{width:165px;height:117px;border:2px solid #fff;position:relative;box-shadow:0 1px 3px rgba(0,0,0,.15)}
.tile span{position:absolute;left:0;right:0;bottom:0;height:20px;background:rgba(40,170,220,.85);color:#fff;font-size:12px;text-align:center;line-height:20px}
.arrow{position:absolute;top:103px;color:#999;font-size:20px}
.footer{position:absolute;top:1093px;left:0;width:882px;height:107px;background:var(--dark);border-bottom:3px solid var(--blue);text-align:center}
.footer .fbrand{margin-top:17px;font-size:22px;font-weight:700;color:var(--red)}
.footer ul{list-style:none;display:flex;justify-content:center;margin-top:12px}
.footer li{font-size:9px;color:#fff;font-weight:700;padding:0 8px;border-right:1px solid #555}
.footer li:last-child{border:none}
.footer li.active{color:var(--blue);font-weight:400}
.footer p{font-size:8.5px;color:#aaa;margin-top:12px}
</style>
</head>
<body>
<div class="page">
  <header class="header">
    <div class="brand"><span class="brand-mark"></span>Brindle Structures</div>
    <div class="call"><em>Call us TODAY !</em>
      <span class="phone"><svg width="12" height="12" viewBox="0 0 24 24"><path fill="#1b9ad6" d="M6.6 10.8a15 15 0 0 0 6.6 6.6l2.2-2.2c.3-.3.7-.4 1-.2 1.1.4 2.3.6 3.6.6.6 0 1 .4 1 1V20c0 .6-.4 1-1 1A17 17 0 0 1 3 4c0-.6.4-1 1-1h3.5c.6 0 1 .4 1 1 0 1.3.2 2.5.6 3.6.1.3 0 .7-.2 1z"/></svg>+123 555 0147</span>
    </div>
  </header>
  <nav class="nav"><ul>
    <li class="active">HOME</li><li>PORTFOLIO</li><li>PRODUCT SPECS</li><li>TESTIMONIALS</li><li>OUR PROCESS</li><li>CONTACT US</li>
  </ul></nav>
  <section class="hero">
    <div class="hero-photo" role="img" aria-label="Businessman holding a glowing blue wireframe house over a city skyline outline"></div>
    <h1>Building Dreams, So You Can<br>Build Memories</h1>
    <svg width="882" height="60" viewBox="0 0 882 60"><path d="M0 10 Q441 80 882 10 L882 60 L0 60Z" fill="#fff"/><path d="M0 10 Q441 80 882 10" fill="none" stroke="#d9261c" stroke-width="4"/></svg>
    <div class="dots"><span class="on"></span><span></span><span></span><span></span></div>
  </section>
  <section class="welcome">
    <h2>WELCOME TO <b>BRINDLE STRUCTURES</b></h2>
    <p>Lorem ipsum dolor sit amet, consectetur adipiscing elit. Praesent volutpat ultricies euismod. Mauris consectetur tellus quis sem dictum pharetra. Nullam euismod nunc blandit mi sagittis, et posuere nunc iaculis. Aenean in sollicitudin quam, non accumsan ipsum. Vivamus in aliquet ex. Nullam malesuadammodo mi, tristique faucibus nisl condimentum condimentum. Duis porttitor nisi ut elementum so</p>
    <span class="more">READ MORE</span>
  </section>
  <section class="cards">
    <article class="card">
      <div class="card-title"><span class="icon"><svg width="14" height="14" viewBox="0 0 24 24"><path fill="#fff" d="M3 10v4h4l6 5V5L7 10zM16 8v8c2-1 3-2.5 3-4s-1-3-3-4z"/></svg></span>LATEST NEWS</div>
      <div class="news"><div class="date">22<small>JULY</small></div><div><h4>Vero eros accumsaet odio</h4><p>quis nostrud exetiperj suscipit lobtis nisl ut aliquip ex ea commod</p></div></div>
      <div class="news"><div class="date">22<small>JULY</small></div><div><h4>Eros accumsaet iusto odio</h4><p>quis nostrud exetiperj suscipit lobtfis nisl ut aliquip exea commod</p></div></div>
      <div class="news"><div class="date">22<small>JULY</small></div><div><h4>Croeros accumsaet iusto odio</h4><p>quis nostrud exetiperj suscipit lobtisf nisl ut aliquip ex commod</p></div></div>
      <div class="link">READ MORE ⊕</div>
    </article>
    <article class="card">
      <div class="card-title"><span class="icon"><svg width="13" height="13" viewBox="0 0 24 24"><rect x="3" y="5" width="18" height="16" rx="2" fill="none" stroke="#fff" stroke-width="2"/><path d="M3 9h18M8 3v4M16 3v4" stroke="#fff" stroke-width="2"/></svg></span>WHAT WE DO</div>
      <div class="task"><svg width="10" height="10" viewBox="0 0 24 24"><path d="M3 13l6 6L21 5" fill="none" stroke="#2a9a7a" stroke-width="4"/></svg><div><h4>Vulputate Molestie Consequat</h4><p>quis nostrud exsetiperj aliquip commod consequa uisquis nostru suscipit nisl roli aliquip exea commod</p><div class="link">KNOW MORE</div></div></div>
      <div class="task"><svg width="10" height="10" viewBox="0 0 24 24"><path d="M3 13l6 6L21 5" fill="none" stroke="#2a9a7a" stroke-width="4"/></svg><div><h4>Vulputate Molestie Consequat</h4><p>quis nostrud exetiperj saliquip commodr consequa uisquis nostru iexetip suscipitt lobtis nisl ut aliquip exea commod</p><div class="link">KNOW MORE</div></div></div>
    </article>
    <article class="card">
      <div class="card-title"><span class="icon"><svg width="14" height="14" viewBox="0 0 24 24"><ellipse cx="12" cy="11" rx="9" ry="7" fill="none" stroke="#fff" stroke-width="2"/><path d="M6 16l-2 5 6-3" fill="#fff"/></svg></span>TESTIMONIALS</div>
      <div class="person"><div class="avatar" role="img" aria-label="Portrait photo of the client"></div><div><b>Arlo Penwick</b><span>Bussiness Man</span></div></div>
      <div class="quote">“ Ut wisi enim ad minim veniam, quism nostrli erci tation ullamcorper suscipitop lobortis commodo ” consequat.<div class="qd"><i></i><i class="on"></i><i></i><i></i></div></div>
    </article>
  </section>
  <section class="types">
    <div class="ribbon">BUILDING TYPES</div>
    <span class="arrow" style="left:78px">‹</span>
    <div class="gallery">
      <div class="tile" role="img" aria-label="Farm shop buildings photo" style="background:linear-gradient(#c9ccc9 45%,#8e8a7c 45%,#6d7f5a)"><span>Farm Shops</span></div>
      <div class="tile" role="img" aria-label="Machine storage shed photo" style="background:linear-gradient(#b9cde0 30%,#7f8a8e 30%,#5e6a55)"><span>Machine Storage</span></div>
      <div class="tile" role="img" aria-label="Seed dealership building photo" style="background:linear-gradient(#cfdbe6 35%,#c8cbc3 35%,#7c8c7a)"><span>Seed Dealership</span></div>
      <div class="tile" role="img" aria-label="Dairy barn aerial photo" style="background:linear-gradient(#6f9a4a 25%,#b9a070 25%,#8d8f86 70%,#5f8d3c)"><span>Dairy</span></div>
    </div>
    <span class="arrow" style="left:794px">›</span>
  </section>
  <footer class="footer">
    <div class="fbrand">Brindle Structures</div>
    <ul><li class="active">HOME</li><li>PORTFOLIO</li><li>PRODUCT SPACS</li><li>TESTIMONIALS</li><li>OUR PROCESS</li><li>CONTACT US</li></ul>
    <p>Copyright © 2015 Brindle Structures &nbsp;| All Rights Reserved</p>
  </footer>
</div>
</body>
</html>
```